Modern multimedia website for Brindle Legal

Website required for a Maritime Law practice in Australia - to modernise old existing one see www.brindlelegal-example.com

Requires resizable website suitable for web, desktop, Phone and Tablet viewing.

Site has to be uncluttered, clear, elegant and modern. Has to instil, confidence, knowledge, trust. An not appear like a stuffy conservative firm.

Logo already designed (attached).

Colours - any suitable to purpose and design.

Would like to display RSS feed(s) but not essential.

Would also like to have a blog component that links to Net Wrk, Chirpa, Snapvue, Zandle + (Accounts already exist).

Already have Domain registered - Need to be able to upload files easily

All Website passwords (uploading etc) to remain with Brindle Legal.

Have attached own images (with identification and trade mark images removed for possible use.)

No images or text to be used that is protected by others copy-write or trademark to be used.

Text for web site to be provided , can be suggested or modification of current website text - am flexible

Target Market(s)

Professional organisations - Shipowners, Operators, Global companies. Luxury Yacht owners,

Industry/Entity Type

Legal

Coding

Coded - Design and coding required

Number of Pages Required

1 page

Requirements
Must have
• Be easy for me to upload to domain server - i am not a computer person.
• Site to be modern style ( flexible with page number) but must be easy and quick to load .
Nice to have
• RSS Feed with feeds from : Harrow's Ledger QMT, vBosun & Coastal -Bulletin.
Should not have
• Look like a conservative Law form.

```html
<!DOCTYPE html>
<html lang="en">
<head>
<meta charset="utf-8">
<title>Brindle Legal – Admiralty and Maritime Lawyers</title>
<link href="https://fonts.googleapis.com/css2?family=Lato:wght@300;400;700&display=swap" rel="stylesheet">
<style>
:root{
  --blue:#1a87c9;
  --blue-dark:#126ba3;
  --ink:#2b2b2b;
  --muted:#9a9a9a;
  --line:#dcdcdc;
  --header:#e9e9e9;
  --band:#efefef;
  --white:#ffffff;
  --footer:#1e252d;
  --footer-base:#14181d;
  --icon-grey:#8c8c8c;
}
*{box-sizing:border-box;margin:0;padding:0}
html,body{width:1200px;height:2844px;overflow:hidden}
body{font-family:'Lato',Arial,sans-serif;color:var(--ink);background:var(--white);position:relative}
section,header,footer{position:absolute;left:0;width:1200px}
.abs{position:absolute}
a{color:inherit;text-decoration:none}
.center{text-align:center;left:0;width:1200px}

/* header */
.site-header{top:0;height:136px;background:var(--header)}
.brand{left:150px;top:58px;width:140px;text-align:center}
.brand-name{font-size:22px;font-weight:400;color:var(--blue-dark);display:block}
.brand-tag{font-size:10px;color:#333;line-height:12px;display:block;margin-top:2px}
.topbar-mail{left:640px;top:16px;display:flex;align-items:center;gap:8px;font-size:12px;color:var(--blue)}
.topbar-mail .ring{width:22px;height:22px;border:1px solid #b8b8b8;border-radius:50%;display:flex;align-items:center;justify-content:center}
.topbar-mail span{text-decoration:underline}
.topbar-divider{left:836px;top:12px;width:1px;height:36px;background:#c4c4c4}
.topbar-social{left:852px;top:20px;display:flex;gap:9px;font-size:11px;color:#666}
.topbar-social span{border:1px solid #b8b8b8;border-radius:12px;padding:4px 7px}
.main-nav{top:80px;left:387px;display:flex;font-size:15px;color:#333}
.main-nav a{position:absolute;white-space:nowrap}
.main-nav a.active{color:var(--blue)}
.btn-consult{left:893px;top:76px;width:152px;height:32px;background:var(--blue);color:#fff;font-size:10px;display:flex;align-items:center;justify-content:center;border:1px solid #5fb0e2}

/* hero */
.hero{top:136px;height:393px;background:linear-gradient(180deg,#5d6670 0%,#3d444c 45%,#22272d 100%)}
.hero-title{top:118px;font-size:32px;line-height:40px;color:#fff;font-weight:400}
.btn-ghost{left:535px;top:224px;width:129px;height:40px;border:1px solid #fff;color:#fff;font-size:13px;display:flex;align-items:center;justify-content:center;background:rgba(0,0,0,.25)}
.hero-arrow{top:170px}

/* welcome */
.welcome{top:529px;height:351px;background:var(--white)}
.welcome-mark{left:576px;top:52px;width:48px;height:48px;border:2px solid var(--blue);border-radius:50%}
.welcome h1{top:142px;font-size:24px;font-weight:400}
.welcome p{top:190px;font-size:11px;line-height:18px;color:var(--muted)}
.btn-split{display:flex;height:34px;border:1px solid #c9c9c9;background:#fff;font-size:11px;color:#333}
.btn-split .label{flex:1;display:flex;align-items:center;justify-content:center}
.btn-split .tab{width:32px;background:var(--blue);display:flex;align-items:center;justify-content:center;color:#fff;font-size:13px;font-weight:700}
.welcome .btn-split{left:537px;top:269px;width:127px}

/* why choose */
.why{top:880px;height:417px;background:var(--band)}
.section-title{font-size:24px;font-weight:400}
.why .section-title{top:44px}
.feature{top:146px;width:281px;height:222px;border:1px solid var(--line);text-align:center}
.feature-icon{position:absolute;left:91px;top:-48px;width:98px;height:98px;border-radius:50%;border:1px solid var(--line);background:var(--band);display:flex;align-items:center;justify-content:center}
.feature h3{margin-top:72px;font-size:20px;font-weight:400}
.feature p{margin:18px auto 0;width:240px;font-size:11px;line-height:18px;color:var(--muted)}
.btn-blue{position:absolute;left:68px;top:188px;width:144px;height:33px;background:var(--blue);color:#fff;font-size:11px;font-weight:700;display:flex;align-items:center;justify-content:center}

/* services */
.services{top:1297px;height:464px;background:var(--white)}
.services .section-title{top:40px}
.services .subtitle{top:80px;font-size:11px;color:var(--muted)}
.service{top:125px;width:205px;height:290px;border:1px solid #eeeeee;text-align:center;background:#fff}
.service.is-active{background:#ececec}
.service-head{height:42px;display:flex;align-items:center;justify-content:center;font-size:17px;color:#222}
.is-active .service-head{background:var(--blue);color:#fff}
.service-band{height:53px;background:#ececec}
.is-active .service-band{background:var(--blue)}
.service-icon{position:absolute;left:58px;top:52px;width:88px;height:88px;border-radius:50%;background:var(--icon-grey);border:4px solid #f5f5f5;display:flex;align-items:center;justify-content:center}
.is-active .service-icon{background:var(--blue)}
.service p{margin:63px auto 0;width:180px;font-size:11px;line-height:18px;color:var(--muted)}
.service .btn-split{position:absolute;left:38px;top:232px;width:128px;height:33px}
.service .btn-split .tab{background:var(--icon-grey)}
.service.is-active .btn-split .tab{background:var(--blue)}
.carousel-arrow{font-size:30px;color:#555;font-weight:300}

/* blog */
.blog{top:1761px;height:393px;background:linear-gradient(180deg,#1f262e 0%,#2f3944 50%,#1a2027 100%)}
.blog h2{left:155px;top:62px;width:400px;font-size:24px;line-height:33px;color:#fff;font-weight:700}
.blog .intro{left:155px;top:138px;width:420px;font-size:11px;line-height:17px;color:#fff}
.btn-dark{left:155px;top:236px;width:177px;height:34px;display:flex;background:#fff;font-size:12px}
.btn-dark .label{flex:1;display:flex;align-items:center;justify-content:center}
.btn-dark .tab{width:40px;background:var(--blue);color:#fff;display:flex;align-items:center;justify-content:center;font-weight:700}
.blog-social{left:155px;top:306px;display:flex;gap:26px;font-size:11px;color:#fff}
.blog-social .active{color:var(--blue)}
.post{left:588px;width:457px;height:80px;background:#f3f3f3;display:flex}
.post-date{width:51px;display:flex;flex-direction:column}
.post-date .day{height:30px;background:var(--blue);color:#fff;font-size:16px;font-weight:700;display:flex;align-items:center;justify-content:center}
.post-date .mon{height:16px;background:#777;color:#fff;font-size:9px;display:flex;align-items:center;justify-content:center}
.post-body{padding:10px 18px;font-size:11px;line-height:15px;color:#333}
.post-body a{display:block;margin-top:8px;color:var(--blue);font-size:11px}

/* testimonial */
.testimonial{top:2154px;height:373px;background:var(--white)}
.testimonial .section-title{top:44px}
.rule{left:309px;width:584px;height:1px;background:var(--line)}
.quote-mark{left:582px;top:90px;width:36px;height:30px;background:#fff;display:flex;justify-content:center}
.testimonial p{top:144px;font-size:11px;line-height:18px;color:var(--muted)}
.avatar{left:566px;top:218px;width:68px;height:68px;border-radius:50%;background:linear-gradient(180deg,#c9a891,#8a6a55);border:3px solid #fff;box-shadow:0 0 0 1px var(--line)}
.person{top:298px;font-size:11px;line-height:15px}
.person b{color:var(--blue);display:block}
.person span{color:var(--muted)}

/* footer */
.site-footer{top:2527px;height:228px;background:linear-gradient(180deg,#252d36,#1b2128)}
.footer-col{top:40px;color:#fff}
.footer-col h4{font-size:13px;font-weight:700;padding-bottom:6px;border-bottom:2px solid var(--blue);display:inline-block}
.footer-col ul{list-style:none;margin-top:14px;font-size:11px;line-height:19px}
.footer-col ul li::before{content:"›";margin-right:8px;font-weight:700}
.news-item{display:flex;gap:12px;margin-top:14px;font-size:10px;line-height:13px;width:220px}
.news-thumb{width:28px;height:22px;flex:none;border:1px solid #9aa5b1}
.contact-row{display:flex;gap:14px;align-items:flex-start;font-size:10px;line-height:13px;margin-top:14px;width:200px}
.contact-row a{color:var(--blue);text-decoration:underline}
.signup-input{margin-top:14px;width:213px;height:28px;background:#fff;font-size:9px;color:#666;display:flex;align-items:center;padding-left:10px}
.btn-send{margin-top:8px;width:84px;height:28px;background:var(--blue);font-size:11px;display:flex;align-items:center;justify-content:center}
.footer-social{margin-top:12px;display:flex;gap:12px;font-size:10px}
.footer-base{top:2755px;height:89px;background:var(--footer-base);color:#fff;font-size:10px}
.footer-base .copy{left:155px;top:28px}
.footer-base .legal{left:155px;top:52px;color:#6b7480}
.footer-base .links{left:836px;top:28px}
</style>
</head>
<body>

<header class="site-header">
  <div class="abs brand">
    <span class="brand-name">Brindle Legal</span>
    <span class="brand-tag">Admiralty and Maritime<br>lawyers</span>
  </div>
  <div class="abs topbar-mail">
    <div class="ring"><svg width="12" height="9" viewBox="0 0 12 9"><rect x=".5" y=".5" width="11" height="8" fill="none" stroke="#999"/><path d="M.5 .5 6 5l5.5-4.5" fill="none" stroke="#999"/></svg></div>
    <span>enquiry@brindlelegal-example.com</span>
  </div>
  <div class="abs topbar-divider"></div>
  <div class="abs topbar-social"><span>Folio</span><span>Chirpa</span><span>Net Wrk</span><span>Mail</span><span>Zandle +</span></div>
  <nav class="abs main-nav">
    <a class="active" style="left:0">Home</a>
    <a style="left:79px">About Us</a>
    <a style="left:182px">Blog</a>
    <a style="left:252px">Links</a>
    <a style="left:326px">Contact Us</a>
  </nav>
  <a class="abs btn-consult">» Request a Free Consultation</a>
</header>

<section class="hero" role="img" aria-label="Photograph of a luxury motor yacht moored in a marina at dusk">
  <h2 class="abs center hero-title">Brindle Legal Provides Admiralty &amp; Maritime<br>Legal Advice Services</h2>
  <a class="abs btn-ghost">Explore More</a>
  <svg class="abs hero-arrow" style="left:104px" width="26" height="54" viewBox="0 0 26 54"><path d="M24 2 3 27l21 25" fill="none" stroke="#fff" stroke-width="4"/></svg>
  <svg class="abs hero-arrow" style="left:1070px" width="26" height="54" viewBox="0 0 26 54"><path d="M2 2l21 25L2 52" fill="none" stroke="var(--blue)" stroke-width="4"/></svg>
</section>

<section class="welcome">
  <div class="abs welcome-mark"></div>
  <h1 class="abs center">Welcome to Brindle Legal</h1>
  <p class="abs center">Brindle Legal is a boutique law practice specializing in Admiralty and Maritime legal advice and litigation services.<br>Our Principal legal practitioner is a uniquely experienced Master Mariner and legal practitioner<br>that began a career in the maritime industry since 1989.</p>
  <a class="abs btn-split"><span class="label">Read More</span><span class="tab">»</span></a>
</section>

<section class="why">
  <h2 class="abs center section-title">Why Choose Us?</h2>
  <div class="abs feature" style="left:155px">
    <div class="feature-icon"><svg width="48" height="44" viewBox="0 0 48 44"><path d="M2 20 46 2 36 42 22 30 38 10 16 27Z" fill="var(--blue)"/><path d="M16 27l2 13 5-9" fill="var(--blue-dark)"/></svg></div>
    <h3>International Shipping</h3>
    <p>Contrary to popular belief, Lorem Ipsum is not simply random text. It has roots in a piece of classical Latin literature from</p>
    <a class="btn-blue">Read More »</a>
  </div>
  <div class="abs feature" style="left:459px">
    <div class="feature-icon"><svg width="20" height="44" viewBox="0 0 20 44"><circle cx="11" cy="6" r="5" fill="var(--blue)"/><path d="M3 16h12v22h4v5H2v-5h4V21H3z" fill="var(--blue)"/></svg></div>
    <h3>Emergency Response</h3>
    <p>Contrary to popular belief, Lorem Ipsum is not simply random text. It has roots in a piece of classical Latin literature from</p>
    <a class="btn-blue">Read More »</a>
  </div>
  <div class="abs feature" style="left:762px">
    <div class="feature-icon"><svg width="52" height="46" viewBox="0 0 52 46"><rect x="20" y="2" width="6" height="8" fill="var(--blue)"/><rect x="28" y="2" width="6" height="8" fill="var(--blue)"/><rect x="12" y="11" width="28" height="10" fill="none" stroke="var(--blue)" stroke-width="3"/><path d="M3 23h46l-7 14H10z" fill="var(--blue)"/><path d="M2 42c6-4 10 4 16 0s10 4 16 0 10 4 16 0" fill="none" stroke="var(--blue)" stroke-width="3"/></svg></div>
    <h3>Marine Accident</h3>
    <p>Contrary to popular belief, Lorem Ipsum is not simply random text. It has roots in a piece of classical Latin literature from</p>
    <a class="btn-blue">Read More »</a>
  </div>
</section>

<section class="services">
  <h2 class="abs center section-title">Our Services</h2>
  <p class="abs center subtitle">We are able to assist by providing cost efficient and effective legal services in relation to</p>
  <span class="abs carousel-arrow" style="left:116px;top:248px">❮</span>
  <span class="abs carousel-arrow" style="left:1064px;top:248px;color:var(--blue)">❯</span>

  <div class="abs service" style="left:155px">
    <div class="service-head">Admiralty Arrests</div><div class="service-band"></div>
    <div class="service-icon"><svg width="40" height="42" viewBox="0 0 40 42"><circle cx="20" cy="6" r="4" fill="none" stroke="#fff" stroke-width="3"/><path d="M20 10v30M11 16h18M4 24c0 9 7 16 16 16s16-7 16-16" fill="none" stroke="#fff" stroke-width="3.5"/></svg></div>
    <p>Contrary to popular belief, Lorem Ipsum is not simply random has roots in a piece of</p>
    <a class="btn-split"><span class="label">Read More</span><span class="tab">»</span></a>
  </div>
  <div class="abs service is-active" style="left:383px">
    <div class="service-head">Marine Inquiries</div><div class="service-band"></div>
    <div class="service-icon"><svg width="44" height="42" viewBox="0 0 44 42"><rect x="16" y="2" width="12" height="7" fill="none" stroke="#fff" stroke-width="2.5"/><path d="M10 10h24v10" fill="none" stroke="#fff" stroke-width="2.5"/><path d="M10 10v10M3 20h38l-6 12H9z" fill="none" stroke="#fff" stroke-width="2.5"/><path d="M2 38c5-3 8 3 13 0s8 3 13 0 8 3 13 0" fill="none" stroke="#fff" stroke-width="2.5"/></svg></div>
    <p>Contrary to popular belief, Lorem Ipsum is not simply random has roots in a piece of</p>
    <a class="btn-split"><span class="label">Read More</span><span class="tab">»</span></a>
  </div>
  <div class="abs service" style="left:610px">
    <div class="service-head">Government policy</div><div class="service-band"></div>
    <div class="service-icon"><svg width="40" height="40" viewBox="0 0 40 40"><path d="M20 2 2 11h36z" fill="#fff"/><rect x="6" y="14" width="4" height="18" fill="#fff"/><rect x="14" y="14" width="4" height="18" fill="#fff"/><rect x="22" y="14" width="4" height="18" fill="#fff"/><rect x="30" y="14" width="4" height="18" fill="#fff"/><rect x="2" y="34" width="36" height="4" fill="#fff"/></svg></div>
    <p>Contrary to popular belief, Lorem Ipsum is not simply random has roots in a piece of</p>
    <a class="btn-split"><span class="label">Read More</span><span class="tab">»</span></a>
  </div>
  <div class="abs service" style="left:840px">
    <div class="service-head">Superyachts</div><div class="service-band"></div>
    <div class="service-icon"><svg width="44" height="38" viewBox="0 0 44 38"><path d="M22 2v10M12 16h20l4 6H8z" fill="#fff" stroke="#fff" stroke-width="2"/><path d="M3 24h38l-6 10H9z" fill="#fff"/></svg></div>
    <p>Contrary to popular belief, Lorem Ipsum is not simply random has roots in a piece of</p>
    <a class="btn-split"><span class="label">Read More</span><span class="tab">»</span></a>
  </div>
</section>

<section class="blog" role="img" aria-label="Dark photograph of a city marina with moored boats behind the blog feature">
  <h2 class="abs">Read our expertly written blog or follow us on social media</h2>
  <p class="abs intro">Lorem ipsum dolor sit amet, consectetur adipiscing elit. Nam sed ligula odio. Sed id metus felis. Ut pretium nisl non justo condimentum id tincidunt nunc faucibus. Ut neque eros, pulvinar eu blandit quis, lacinia nec ipsum. Etiam vel orci ipsum. Sed eget velit ipsum.</p>
  <a class="abs btn-dark"><span class="label">Contact Us Now</span><span class="tab">»</span></a>
  <div class="abs blog-social"><span>Snapvue</span><span class="active">Chirpa</span><span>Zandle +</span><span>Net Wrk</span></div>

  <article class="abs post" style="top:57px">
    <div class="post-date"><span class="day">18</span><span class="mon">Aug</span></div>
    <div class="post-body">Lorem ipsum dolor sit amet, consectetur adipiscing elit.<br>Nam sed ligula odio. Sed id metus felis.<a>Read More »</a></div>
  </article>
  <article class="abs post" style="top:148px">
    <div class="post-date"><span class="day">15</span><span class="mon">Aug</span></div>
    <div class="post-body">Lorem ipsum dolor sit amet, consectetur adipiscing elit.<br>Nam sed ligula odio. Sed id metus felis.<a>Read More »</a></div>
  </article>
  <article class="abs post" style="top:239px">
    <div class="post-date"><span class="day">10</span><span class="mon">Aug</span></div>
    <div class="post-body">Lorem ipsum dolor sit amet, consectetur adipiscing elit.<br>Nam sed ligula odio. Sed id metus felis.<a>Read More »</a></div>
  </article>
</section>

<section class="testimonial">
  <h2 class="abs center section-title">Our Testimonial</h2>
  <div class="abs rule" style="top:104px"></div>
  <div class="abs quote-mark"><svg width="28" height="26" viewBox="0 0 28 26"><path d="M14 1C6 1 1 5 1 11c0 4 2 7 6 9l-2 5 7-4h2c8 0 13-4 13-10S22 1 14 1z" fill="var(--blue)"/><text x="14" y="17" font-family="Lato,sans-serif" font-size="14" font-weight="700" fill="#fff" text-anchor="middle">”</text></svg></div>
  <p class="abs center">I must explain to you how all this mistaken idea of denouncing pleasure<br>and praising pain was born and I will give you a complete account of the system,<br>expoundactual teachings of the great , the master happiness.</p>
  <span class="abs carousel-arrow" style="left:266px;top:160px;color:#888">❮</span>
  <span class="abs carousel-arrow" style="left:914px;top:160px;color:var(--blue)">❯</span>
  <div class="abs rule" style="top:252px"></div>
  <div class="abs avatar" role="img" aria-label="Portrait photograph of the client giving the testimonial"></div>
  <div class="abs center person"><b>Mistaken</b><span>Teachings of the great</span></div>
</section>

<footer class="site-footer" role="img" aria-label="Dark harbour photograph behind the footer">
  <div class="abs footer-col" style="left:155px">
    <h4>Quick Links</h4>
    <ul><li>Home</li><li>About Us</li><li>Blog</li><li>Links</li><li>Contact Us</li></ul>
  </div>
  <div class="abs footer-col" style="left:318px">
    <h4>Recent News</h4>
    <div class="news-item"><span class="news-thumb"></span><span>Maecenas etos sit amet, consectetur adipis cing elit. Terminal volutpat rutrum metro</span></div>
    <div class="news-item"><span class="news-thumb"></span><span>Maecenas etos sit amet, consectetur adipis cing elit. Terminal volutpat rutrum metro</span></div>
  </div>
  <div class="abs footer-col" style="left:590px">
    <h4>Contact Us</h4>
    <div class="contact-row"><svg width="12" height="16" viewBox="0 0 12 16"><path d="M6 0a6 6 0 0 0-6 6c0 4.5 6 10 6 10s6-5.5 6-10a6 6 0 0 0-6-6z" fill="var(--blue)"/><circle cx="6" cy="6" r="2.2" fill="#1e252d"/></svg><span>Lorem ipsum dolor sit amet consectetur adipiscing elit, sed do</span></div>
    <div class="contact-row"><svg width="12" height="14" viewBox="0 0 12 14"><path d="M2 0h3l1 4-2 1c1 2 2 4 4 5l1-2 3 1v3c-6 1-11-6-10-12z" fill="var(--blue)"/></svg><span>+123-456-7890</span></div>
    <div class="contact-row"><svg width="14" height="10" viewBox="0 0 14 10"><rect x=".5" y=".5" width="13" height="9" fill="none" stroke="var(--blue)"/><path d="M.5 .5 7 6l6.5-5.5" fill="none" stroke="var(--blue)"/></svg><a>info@harbourline-example.com</a></div>
  </div>
  <div class="abs footer-col" style="left:832px">
    <h4>News Sign Up</h4>
    <div class="signup-input">Enter Your Email Address</div>
    <div class="btn-send">Send ➤</div>
    <div class="footer-social"><span>Snapvue</span><span>Chirpa</span><span>Zandle +</span><span>Net Wrk</span></div>
  </div>
</footer>

<div class="abs footer-base" style="left:0;width:1200px">
  <span class="abs copy">Copyright © 2015 Brindle Legal</span>
  <span class="abs legal">Limitation of liability in accordance with legal practitioners liability legislation.</span>
  <span class="abs links">Disclaimer &amp; Use Terms &nbsp;|&nbsp; Privacy Policy</span>
</div>

</body>
</html>
```